Stationary Set and Logo Update **PAYMENT GUARANTEED**

Stationery Design and Logo Update

About Us

Trindex Supply is a wholesale distributor of OEM [original brand] and compatible [generic brand] parts and supplies for use in copiers, faxes, printers, and multi-function machines. In plain English…we sell all the parts and supplies [such as toner] that make up any office equipment which outputs an image on paper.

Trindex was the 1st distributor to develop and sell a generic brand copier part in the United States. We have been in business since 1972 [nearly 40 years]. Our tagline is "The Steady Choice," as in our company was the first alternative product that copier dealers had to buying original brand copier parts. Trindex is known for offering reliable and cost-effective OEM and compatible products.

Project

We require a fresh, modern and corporate identity. Please submit a stationary package inclusive of a double-sided business card (2" x 3.5"), letterhead (8.5'x11"), and standard #10 envelope (4-1/8” x 9-1/2). You may use our current logo or preferably your take on an updated one. If an attempt is made in updating the logo #004D8E or a similar hue should be used as the primary color.

The design should be clean, simple, modern and professional and make an immediate impact.

Target Market(s)

Copier and printer dealers who lease and service imaging equipment in the United States and Latin America.

Industry/Entity Type

Business

Requirements
Must have
• Simple, clean, modern and professional. Please use #004D8E or a similar hue as the primary color. Letterhead must accommate (2) addresses. We have 2 locations.
Nice to have
• A simple, modern update to our current logo. https://assets.mailvorbo.example/fs030/5520384417702/img/418.jpg
Should not have
• More than (2) colors on logo.

```html
<!DOCTYPE html>
<html lang="en">
<head>
<meta charset="utf-8">
<title>Trindex Supply – Stationery Set</title>
<link rel="stylesheet" href="https://fonts.googleapis.com/css2?family=Questrial&family=Dawning+of+a+New+Day&display=swap">
<style>
  :root{
    --lime:#bff200;
    --blue:#0c5193;
    --navy:#0b2d57;
    --ink:#1b1b1b;
    --paper:#ffffff;
    --page-bg:#ffffff;
    --shade:#cfcfcf;
  }
  *{box-sizing:border-box;margin:0;padding:0}
  html,body{width:1200px;height:900px;overflow:hidden;background:var(--page-bg)}
  body{position:relative;font-family:"Questrial",sans-serif;color:var(--navy)}

  .board{position:absolute;left:20px;top:18px;width:1140px;height:844px;border-radius:64px;background:var(--paper);box-shadow:0 2px 14px rgba(0,0,0,.28)}

  /* Letterhead */
  .letterhead{position:absolute;left:118px;top:35px;width:622px;height:803px;background:var(--paper);box-shadow:2px 3px 6px rgba(0,0,0,.35)}
  .letterhead__band{position:absolute;left:0;top:0;width:622px;height:130px}
  .letterhead__main-address{position:absolute;left:14px;top:13px;font-size:10px;line-height:13px;color:var(--navy)}
  .letterhead__branch-address{position:absolute;left:14px;top:74px;width:105px;text-align:right;font-size:10px;line-height:12.5px;color:var(--blue)}
  .letterhead__brand{position:absolute;right:20px;top:24px;text-align:right}
  .brand-name{font-family:"Questrial",sans-serif;color:var(--navy);letter-spacing:-.5px;line-height:1}
  .letterhead__brand .brand-name{font-size:36px}
  .letterhead__tagline{font-size:13px;color:var(--blue);margin-top:5px}

  .letter{position:absolute;left:77px;top:150px;width:462px;font-family:"Dawning of a New Day",cursive;color:var(--ink)}
  .letter__greeting{font-size:24px;margin-bottom:22px}
  .letter__body p{font-size:12.5px;line-height:16.2px;margin-bottom:16px;text-align:justify}
  .letter__closing{position:absolute;left:462px;top:666px;font-family:"Dawning of a New Day",cursive;font-size:12px;color:var(--ink)}
  .letter__signature{position:absolute;left:458px;top:686px;width:90px;height:62px;background:linear-gradient(135deg,#f3f3f3,#e2e2e2);border-radius:4px}
  .letter__signer{position:absolute;left:500px;top:752px;font-family:"Dawning of a New Day",cursive;font-size:12px;color:var(--ink)}

  .letterhead__footer{position:absolute;left:0;bottom:0;width:622px;height:25px;background:var(--lime);display:flex;justify-content:center;align-items:center;gap:22px;font-size:10px;color:var(--navy)}

  /* Envelope */
  .envelope{position:absolute;left:425px;top:345px;width:693px;height:303px;background:var(--lime);box-shadow:2px 3px 7px rgba(0,0,0,.35)}
  .envelope__return{position:absolute;left:0;top:22px;width:178px;height:78px;background:var(--paper);transform:rotate(-1.5deg);box-shadow:1px 2px 4px rgba(0,0,0,.3);padding:8px 0 0 15px}
  .envelope__return .brand-name{font-size:22px;margin-bottom:3px}
  .envelope__return address{font-style:normal;font-size:10px;line-height:11.5px;color:var(--blue)}
  .envelope__postage{position:absolute;right:18px;top:18px;width:116px;height:44px;background:linear-gradient(90deg,#d8b84a,#e2c96a);opacity:.75;border-radius:2px}
  .envelope__recipient{position:absolute;left:238px;top:151px;width:226px;height:82px;background:var(--paper);box-shadow:1px 2px 4px rgba(0,0,0,.3);padding:18px 0 0 12px}
  .envelope__recipient-name{font-size:14px;color:var(--navy);margin-bottom:2px}
  .envelope__recipient address{font-style:normal;font-size:11px;line-height:12.5px;color:var(--blue)}

  /* Colour palette & logo */
  .palette{position:absolute;left:915px;top:84px;display:flex;gap:33px}
  .palette svg{width:40px;height:62px}
  .brand-mark{position:absolute;left:895px;top:236px}
  .brand-mark .brand-name{font-size:72px}
</style>
</head>
<body>
  <div class="board"></div>

  <section class="letterhead">
    <svg class="letterhead__band" viewBox="0 0 622 130" aria-hidden="true">
      <polygon points="0,0 622,0 622,90 0,127" fill="var(--shade)"/>
      <polygon points="0,0 622,0 622,80 0,122" fill="var(--lime)"/>
    </svg>
    <address class="letterhead__main-address" style="font-style:normal">418 Harbor Ave.<br>Millbrook, USA 20418<br>office@trindexsupply.com</address>
    <address class="letterhead__branch-address" style="font-style:normal">77 Orchard Ln.<br>Fairvale, USA 30577<br>branch@trindexsupply.com</address>
    <div class="letterhead__brand">
      <div class="brand-name">Trindex</div>
      <div class="letterhead__tagline">“the steady choice.”</div>
    </div>

    <article class="letter">
      <p class="letter__greeting">Dear Mark,</p>
      <div class="letter__body">
        <p>Lorem ipsum dolor sit amet, consectetur adipiscing elit. Proin pulvinar elit interdum ligula consectetur ac eleifend odio sollicitudin. In in arcu at dolor fringilla auctor sit amet sit amet dolor. Nam feugiat venenatis tempus. Nam porttitor metus quis purus fermentum vel elementum nunc feugiat. Pellentesque sodales convallis ipsum id blandit. Suspendisse potenti. Mauris quam tellus, blandit ac imperdiet in, gravida et felis. Nulla vel vestibulum magna. Vestibulum ante ipsum primis in faucibus orci luctus et ultrices posuere cubilia Curae; Suspendisse cursus malesuada turpis et vehicula. Nam eu neque ac risus accumsan placerat. Morbi faucibus congue sollicitudin.</p>
        <p>Integer tempus ante tellus, eleifend tempor urna. Vivamus bibendum massa. Morbi imperdiet iaculis turpis, at ultrices ligula sit amet porttitor. Sed ac turpis erat, risus cursus purus aliquam pretium. Class aptent taciti per inceptos himenaeos. In ac nisi tortor. Suspendisse consectetur purus ac risus porttitor a sagittis velit. Phasellus nec orci vel elit convallis iaculis vel a leo. risus aliquet vitae. Pellentesque mauris metus, interdum. Nulla eget condimentum urna. Suspendisse potenti. luctus velit, nec rhoncus felis magna quis mauris.</p>
        <p>Morbi ut nunc at ante feugiat molestie ut lobortis a libero sem. Ut cursus, sem et ornare interdum, elit mi augue. Sed sed felis nec quam rutrum pellentesque. Mauris mattis volutpat erat, eu mollis velit lobortis tellus ligula. Donec ligula enim, egestas varius hendrerit consequat sollicitudin. Nam posuere iaculis lobortis. Sed urna orci, dignissim vitae tincidunt non, adipiscing sit amet mi.</p>
      </div>
    </article>
    <p class="letter__closing">Thanks so Much,</p>
    <div class="letter__signature" role="img" aria-label="Handwritten signature of Nora Castel"></div>
    <p class="letter__signer">Nora Castel</p>

    <footer class="letterhead__footer">
      <span>www.trindexsupply.com</span>
      <span>1-800-874-6339</span>
      <span>All Rights Reserved Copyright 2011</span>
    </footer>
  </section>

  <section class="envelope">
    <div class="envelope__return">
      <div class="brand-name">Trindex</div>
      <address>418 Harbor Ave.<br>Millbrook, USA 20418<br>office@trindexsupply.com</address>
    </div>
    <div class="envelope__postage" role="img" aria-label="Metered postage imprint"></div>
    <div class="envelope__recipient">
      <div class="envelope__recipient-name">Mark Ellison</div>
      <address>52 Quarry Rd.<br>Lakeport, USA &nbsp;75219</address>
    </div>
  </section>

  <div class="palette" aria-label="Brand colours">
    <svg viewBox="0 0 40 62"><path d="M20 0 C26 16 40 30 40 42 A20 20 0 0 1 0 42 C0 30 14 16 20 0Z" fill="var(--lime)"/></svg>
    <svg viewBox="0 0 40 62"><path d="M20 0 C26 16 40 30 40 42 A20 20 0 0 1 0 42 C0 30 14 16 20 0Z" fill="var(--blue)"/></svg>
    <svg viewBox="0 0 40 62"><path d="M20 0 C26 16 40 30 40 42 A20 20 0 0 1 0 42 C0 30 14 16 20 0Z" fill="var(--navy)"/></svg>
  </div>

  <div class="brand-mark"><div class="brand-name">Trindex</div></div>
</body>
</html>
```